Start up in business consultancy needs a business card

We need the business card's layout (we have already the logo). Our business is concerned on consultancy services delivered to companies on the matter of sustainability. Business card should be enough essentials and professional style.

Side A with the following info:
logo + a space for the claim (still to identify) + website of the company

Side B with the following info:
Name of business card holder + title of the business card holder + address of the company + space for mobile number, phone number, fax number + e-mail of business card holder + graphic details around.

Target Market(s)

Business of any sector

Industry/Entity Type

Business Service

Contact Information for Business Card

Name of the company:
Pianoverde srl
Società Benefit

Address of the company:
Via Lucerna, 7
21047 - Saronno (VA)

Website:
www.pianoverde.it

Name of the BC' holder:
Luca Ferentino

Title:
Co-fondatore

Email:
luca@pianoverde.it

Mobile:
+39 348 915 2074
Phone:
+39 348 915 2074
Fax:
+39 348 915 2074

Font styles to use
Other font styles liked:
• new gothic

```html
<!DOCTYPE html>
<html lang="it">
<head>
<meta charset="utf-8">
<title>Pianoverde – biglietto da visita</title>
<link rel="stylesheet" href="https://fonts.googleapis.com/css2?family=Didact+Gothic&family=Montserrat:wght@600;700&display=swap">
<style>
  :root {
    --brand-blue: #166bb0;
    --stripe-grey: #444547;
    --text-grey: #3c3c3c;
    --card-white: #ffffff;
    --backdrop: #e6e3df;
  }
  * { margin: 0; padding: 0; box-sizing: border-box; }
  html, body { width: 1200px; height: 1000px; overflow: hidden; }
  body { background: var(--backdrop); position: relative; font-family: "Didact Gothic", sans-serif; }

  .card {
    position: absolute;
    width: 525px; height: 300px;
    background: var(--card-white);
    box-shadow: 0 6px 18px rgba(0,0,0,.18);
    overflow: hidden;
  }
  .card--front { left: 150px; top: 170px; }
  .card--back  { left: 525px; top: 530px; }

  /* Front */
  .front__band {
    position: absolute; left: 0; top: 0; width: 100%; height: 148px;
    background: var(--brand-blue);
  }
  .front__stripe {
    position: absolute; left: 0; top: 156px; width: 100%; height: 8px;
    background: var(--stripe-grey);
  }
  .front__brand {
    position: absolute; right: 26px; top: 28px;
    display: flex; align-items: center; gap: 10px;
    color: var(--card-white); font-size: 22px;
  }
  .front__brand-circle {
    width: 36px; height: 36px; border: 3px solid var(--card-white); border-radius: 50%;
  }
  .holder { position: absolute; left: 68px; top: 92px; color: var(--card-white); }
  .holder__name { font-family: "Montserrat", sans-serif; font-weight: 700; font-size: 25px; line-height: 1; }
  .holder__title { font-size: 19px; margin-top: 4px; padding-left: 6px; }

  .contacts { position: absolute; top: 196px; display: flex; flex-direction: column; gap: 5px; color: var(--text-grey); font-size: 16px; }
  .contacts--phones { left: 66px; }
  .contacts--place { left: 292px; gap: 14px; }
  .contact { display: flex; align-items: flex-start; gap: 10px; line-height: 1.05; }
  .contact svg { width: 14px; height: 14px; fill: var(--brand-blue); flex: none; margin-top: 2px; }
  .contacts__divider { position: absolute; left: 265px; top: 192px; width: 1px; height: 62px; background: var(--text-grey); }

  /* Back */
  .back__brand {
    position: absolute; left: 22px; top: 226px;
    display: flex; align-items: center; gap: 10px;
    color: var(--brand-blue); font-size: 25px;
  }
  .back__brand-circle { width: 66px; height: 66px; border: 3px solid var(--brand-blue); border-radius: 50%; }
  .back__web {
    position: absolute; left: 285px; top: 230px; width: 240px; height: 34px;
    background: var(--brand-blue); color: var(--card-white);
    font-family: "Montserrat", sans-serif; font-weight: 700; font-size: 15px;
    display: flex; align-items: center; justify-content: center;
  }
</style>
</head>
<body>

<section class="card card--front" aria-label="Fronte del biglietto">
  <div class="front__band"></div>
  <div class="front__stripe"></div>
  <div class="front__brand"><span class="front__brand-circle"></span><span>pianoverde</span></div>
  <div class="holder">
    <p class="holder__name">Luca Ferentino</p>
    <p class="holder__title">Co-fondatore</p>
  </div>

  <div class="contacts contacts--phones">
    <p class="contact"><svg viewBox="0 0 14 14"><path d="M4 0h6a1 1 0 0 1 1 1v12a1 1 0 0 1-1 1H4a1 1 0 0 1-1-1V1a1 1 0 0 1 1-1zm.6 1.5v9.5h4.8V1.5z"/></svg>+39 348 915 2074</p>
    <p class="contact"><svg viewBox="0 0 14 14"><path d="M1 4c0-2 2-3 6-3s6 1 6 3v1.5h-3V4H4v1.5H1zm2 2.5h8l2 5.5H1z"/></svg>+39 348 915 2074</p>
    <p class="contact"><svg viewBox="0 0 14 14"><path d="M3 0h8v4H3zM1 5h12v6h-2v3H3v-3H1zm3 4v4h6V9z"/></svg>+39 348 915 2074</p>
  </div>
  <div class="contacts__divider"></div>
  <div class="contacts contacts--place">
    <p class="contact"><svg viewBox="0 0 14 14"><path d="M7 0a5 5 0 0 1 5 5c0 3.5-5 9-5 9S2 8.5 2 5a5 5 0 0 1 5-5zm0 3a2 2 0 1 0 0 4 2 2 0 0 0 0-4z"/></svg><span>Via Lucerna, 7 , 21047<br>Saronno (VA)</span></p>
    <p class="contact"><svg viewBox="0 0 14 14"><path d="M0 3h14v1L7 8 0 4zm0 2.3l7 4 7-4V11H0z"/></svg>luca@pianoverde.it</p>
  </div>
</section>

<section class="card card--back" aria-label="Retro del biglietto">
  <div class="back__brand"><span class="back__brand-circle"></span><span>pianoverde</span></div>
  <div class="back__web">www.pianoverde.it</div>
</section>

</body>
</html>
```